Business Card for Technology Startup

Design a 2-sided business card using the logo provided. We are a digital healthcare platform that provides a mobile app and web UI that helps caregivers, families, and doctors share information and provide better patient outcomes. We use AI and machine learning to help guide patients through their day-to-day life. The final design should communicate stability, peace, comfort, but also align with the image of an AI-driven technology startup.

I'd like the deliverable to by a Photoshop PSD file (with layers) that I can work with in pixlr.com. Should contain the following editable layers:
Name (ex. Karl Whitby)
Title (ex. Founder / CEO)
Email (ex. info@morventary.ai)
Phone (ex. (999) 482-7160)
Website (ex. https://morventary.ai)

```html
<!DOCTYPE html>
<html lang="en">
<head>
<meta charset="UTF-8">
<title>Morventary Business Card</title>
<link rel="stylesheet" href="https://fonts.googleapis.com/css2?family=Montserrat:wght@400;500;700;800&display=swap">
<style>
  :root {
    --bg: #d2d7d7;
    --card: #f1f1f0;
    --ink: #0b0b0c;
    --muted: #3c3c3e;
    --brand: #1cb8e8;
    --edge: #2bb5e0;
  }
  * { margin: 0; padding: 0; box-sizing: border-box; }
  html, body { width: 1200px; height: 881px; overflow: hidden; }
  body {
    background: var(--bg);
    font-family: "Montserrat", sans-serif;
    display: flex;
    align-items: center;
    justify-content: center;
    gap: 60px;
  }
  .card {
    width: 500px;
    height: 286px;
    background: var(--card);
    border-bottom: 4px solid var(--edge);
    box-shadow: 0 18px 40px rgba(60, 70, 75, 0.22);
    position: relative;
  }
  .wordmark {
    display: flex;
    align-items: center;
    gap: 10px;
    color: var(--ink);
    font-weight: 800;
    letter-spacing: 0.2px;
  }
  .wordmark-dot {
    border-radius: 50%;
    background: var(--brand);
    flex: none;
  }
  /* Front: contact side */
  .card-front .wordmark {
    position: absolute;
    left: 34px;
    top: 118px;
    font-size: 25px;
  }
  .card-front .wordmark-dot { width: 18px; height: 18px; }
  .divider {
    position: absolute;
    left: 268px;
    top: 70px;
    width: 2px;
    height: 146px;
    background: var(--brand);
  }
  .contact {
    position: absolute;
    left: 290px;
    top: 72px;
  }
  .contact-name {
    color: var(--brand);
    font-weight: 700;
    font-size: 22px;
    line-height: 1.1;
  }
  .contact-title {
    color: var(--muted);
    font-size: 12.5px;
    margin-top: 3px;
  }
  .contact-list {
    list-style: none;
    margin-top: 22px;
  }
  .contact-list li {
    display: flex;
    align-items: center;
    gap: 8px;
    color: var(--muted);
    font-size: 12px;
    line-height: 1.75;
  }
  .contact-list svg { width: 11px; height: 11px; fill: var(--brand); flex: none; }
  /* Back: logo side */
  .card-back {
    display: flex;
    align-items: center;
    justify-content: center;
  }
  .card-back .wordmark { font-size: 46px; gap: 16px; }
  .card-back .wordmark-dot { width: 32px; height: 32px; }
</style>
</head>
<body>
  <section class="card card-front">
    <div class="wordmark"><span class="wordmark-dot"></span>morventary</div>
    <div class="divider"></div>
    <div class="contact">
      <p class="contact-name">Karl Whitby</p>
      <p class="contact-title">Founder / CEO</p>
      <ul class="contact-list">
        <li>
          <svg viewBox="0 0 24 24" aria-hidden="true"><path d="M6.6 10.8a15.2 15.2 0 0 0 6.6 6.6l2.2-2.2c.3-.3.7-.4 1-.2 1.1.4 2.3.6 3.6.6.6 0 1 .4 1 1V20c0 .6-.4 1-1 1A17 17 0 0 1 3 4c0-.6.4-1 1-1h3.5c.6 0 1 .4 1 1 0 1.3.2 2.5.6 3.6.1.3 0 .7-.2 1z"/></svg>
          (999) 482-7160
        </li>
        <li>
          <svg viewBox="0 0 24 24" aria-hidden="true"><path d="M2 5h20v14H2z" opacity=".0"/><path d="M3 5h18c.6 0 1 .4 1 1v.4l-10 6.3L2 6.4V6c0-.6.4-1 1-1zm-1 3.7 10 6.3 10-6.3V18c0 .6-.4 1-1 1H3c-.6 0-1-.4-1-1z"/></svg>
          info@morventary.ai
        </li>
        <li>
          <svg viewBox="0 0 24 24" aria-hidden="true"><circle cx="12" cy="12" r="10"/></svg>
          www.morventary.ai
        </li>
      </ul>
    </div>
  </section>
  <section class="card card-back">
    <div class="wordmark"><span class="wordmark-dot"></span>morventary</div>
  </section>
</body>
</html>
```